Traffic product supplier - Temporary Raised Pavement Markers

We need a flyer design that will grab the customer's eye to the product (TRPMs) and entice curiosity to the business. Showing 1 product but promoting other products. The following information should be included:
- Logo (attached)
- Sale Product image (Temporary Road Pavement Marker AKA Press and Holds)
- Product wording (attached word document)

Happy for you to add/amend wording for grammatical purpose and other images that show it is a sale flyer.

Background on KLV - We are a thermoplastic manufacturer for road markings and traffic product supplier. KLV specializes in producing high quality hotmelt thermoplastic that meet Australian Standard AS4049.2. We are able to produce other specifications as required by the customer.

Would like the colour scheme to be similar to the logo.

If you need more information let me know.

Target Market(s)

Asphalt industry / road builders

Font styles to use
Serif
Sans Serif

Requirements
Must have
• - Kelvoro Lane Ventures (My company name)
- Contact details:
- 02 8417 2530
- marcus.t@klvsupplyco.com.au
- info@klvsupplyco.com.au
-www.klvmtq.com

- Attached images.
-Title (Temporary Road Pavement Markers)

```html
<!DOCTYPE html>
<html lang="en">
<head>
<meta charset="utf-8">
<title>KLV Temporary Road Pavement Markers Flyer</title>
<link href="https://fonts.googleapis.com/css2?family=Montserrat:wght@300;400;500;600;700&family=Roboto+Condensed:wght@400;700&display=swap" rel="stylesheet">
<style>
  :root {
    --brand-blue: #2561a4;
    --brand-yellow: #f7cb16;
    --ink: #2a2a2a;
    --paper: #ffffff;
    --strip-grey: #ececec;
    --frame-grey: #cfcfcf;
  }
  * { box-sizing: border-box; margin: 0; padding: 0; }
  html, body { width: 882px; height: 1200px; overflow: hidden; background: var(--paper); }
  body { font-family: "Montserrat", sans-serif; color: var(--ink); }
  .flyer { position: relative; width: 882px; height: 1200px; background: var(--paper); overflow: hidden; }

  .hero-photo { position: absolute; left: 0; top: 0; width: 882px; height: 480px; }
  .hero-photo svg { display: block; }

  .brand-name {
    position: absolute; left: 69px; top: 68px;
    display: flex; align-items: center; gap: 12px;
    font-weight: 700; font-size: 56px; color: var(--paper); letter-spacing: 2px;
  }
  .brand-name .brand-square { width: 22px; height: 22px; background: var(--brand-yellow); }

  .product-shot {
    position: absolute; left: 488px; top: 315px; width: 350px; height: 241px;
    background: linear-gradient(160deg, #f2b81b 0%, #e9ad12 45%, #eeeeee 60%, #dcdcdc 100%);
    border-radius: 4px;
  }

  .headline {
    position: absolute; left: 70px; top: 514px;
    font-weight: 700; font-size: 27px; line-height: 37px; color: var(--brand-blue);
  }
  .headline-rule {
    position: absolute; left: 71px; top: 602px; width: 730px; height: 4px;
    background: linear-gradient(to right, var(--brand-yellow) 0 88px, var(--brand-blue) 88px);
  }
  .intro {
    position: absolute; left: 71px; top: 609px; width: 735px;
    font-size: 14.6px; line-height: 21px; font-weight: 400;
  }
  .intro strong { font-weight: 700; color: #111; }

  .details { position: absolute; left: 73px; top: 693px; width: 372px; font-size: 14.4px; line-height: 19px; }
  .details p + p { margin-top: 10px; }
  .details .accent { color: var(--brand-blue); font-weight: 700; }

  .price { position: absolute; left: 75px; top: 926px; display: flex; align-items: center; height: 28px; }
  .price-amount {
    background: var(--brand-yellow); color: var(--brand-blue);
    font-weight: 700; font-size: 19px; padding: 0 4px; height: 24px; line-height: 24px;
  }
  .slash { width: 3px; height: 26px; background: var(--brand-blue); transform: skewX(-15deg); margin: 0 6px 0 3px; }
  .price-unit { font-family: "Roboto Condensed", sans-serif; font-size: 18px; color: var(--brand-blue); }

  .dims-tab { position: absolute; left: 490px; top: 730px; display: flex; align-items: center; height: 27px; }
  .dims-tab .tab-label {
    background: var(--brand-yellow); color: var(--brand-blue);
    font-weight: 700; font-size: 16px; padding: 0 8px 0 5px; height: 26px; line-height: 27px;
  }
  .dims-box {
    position: absolute; left: 490px; top: 757px; width: 310px; height: 216px;
    background: var(--brand-blue); color: var(--paper); padding: 16px 14px 0 52px;
  }
  .dims-list { list-style: none; position: relative; font-size: 13.6px; line-height: 18px; font-weight: 500; }
  .dims-list li { position: relative; margin-bottom: 7px; }
  .dims-list li::before {
    content: ""; position: absolute; left: -28px; top: 3px; width: 11px; height: 11px;
    border-radius: 50%; background: var(--paper); border: 2.5px solid var(--brand-yellow);
  }
  .dims-line { position: absolute; left: 28px; top: 24px; width: 2px; height: 126px; background: var(--brand-yellow); }

  .range { position: absolute; left: 75px; top: 971px; display: flex; gap: 11px; }
  .range-tile { width: 175px; height: 88px; border: 1px solid var(--frame-grey); padding: 11px 16px; }
  .range-tile div { width: 100%; height: 100%; border-radius: 2px; }
  .tile-round { background: linear-gradient(90deg, #e9461e 0 33%, #23448f 33% 66%, #f4c21a 66%); }
  .tile-flat { background: linear-gradient(90deg, #d8d8d8, #c9a233 50%, #e2e2e2); }
  .tile-adhesive { background: linear-gradient(90deg, #6a5a3f, #2a2a2a 60%, #151515); }
  .tile-glow { background: linear-gradient(90deg, #c9c24a 0 50%, #2f9a7e 50%); }

  .footer-call { position: absolute; left: 0; top: 1110px; width: 882px; height: 90px; }
  .call-text { position: absolute; left: 0; top: 1127px; width: 295px; text-align: center; color: var(--paper); }
  .call-label { font-size: 21px; font-weight: 300; letter-spacing: 1px; line-height: 26px; }
  .call-number { font-size: 27px; font-weight: 700; line-height: 32px; }

  .company { position: absolute; left: 352px; top: 1123px; font-size: 15px; font-weight: 700; color: var(--brand-blue); line-height: 20px; }
  .web-pill {
    position: absolute; left: 664px; top: 1118px; width: 139px; height: 28px;
    background: var(--brand-blue); color: var(--paper); border-radius: 6px 6px 0 0;
    font-size: 13px; font-weight: 700; text-align: center; line-height: 28px; white-space: nowrap;
  }
  .contact-strip {
    position: absolute; left: 310px; top: 1146px; width: 572px; height: 28px;
    background: var(--strip-grey); display: flex; align-items: center; gap: 16px; padding-left: 42px;
    font-size: 12.4px;
  }
  .contact-strip span { display: flex; align-items: center; gap: 6px; white-space: nowrap; }
</style>
</head>
<body>
<main class="flyer">
  <div class="hero-photo" role="img" aria-label="Road crew in high-visibility clothing painting white pedestrian crossing lines on fresh asphalt, with traffic cones">
    <svg width="882" height="480" viewBox="0 0 882 480">
      <defs>
        <linearGradient id="asphalt" x1="0" y1="0" x2="1" y2="1">
          <stop offset="0" stop-color="#2b2b2b"/>
          <stop offset="1" stop-color="#1c1c1c"/>
        </linearGradient>
      </defs>
      <path d="M0 0 H882 V427 H430 C400 427 395 476 360 476 H0 Z" fill="url(#asphalt)"/>
      <path d="M340 476 C378 476 388 427 418 427 L432 427 C402 427 395 476 358 476 Z" fill="var(--brand-blue)"/>
      <path d="M358 476 C395 476 402 427 432 427 L448 427 C415 427 410 476 374 476 Z" fill="var(--brand-yellow)"/>
    </svg>
  </div>

  <div class="brand-name"><span>KLV</span><span class="brand-square"></span></div>

  <div class="product-shot" role="img" aria-label="Yellow and white temporary raised pavement markers with reflective strips"></div>

  <h1 class="headline">Creating a Safe Environment<br>for All Road Users</h1>
  <div class="headline-rule"></div>

  <p class="intro">Temporary road pavement markers, also known as <strong>press 'n' holds,</strong> are a <strong>great short-term solution to mark asphalt and pavements before permanent line marking takes place.</strong> They provide a way to delineate lanes and edges before the permanent longitudinal line marking process takes place.</p>

  <div class="details">
    <p>TRPMs or press 'n' holds are available in <span class="accent">yellow or white and come with a Class 1A reflective strip</span> applied to tough high impact plastic. They are an <span class="accent">economical solution for making newly laid roads safer.</span></p>
    <p>An easy to remove clear cover protects the reflective film during sealing and is easily ripped off afterwards.</p>
  </div>

  <div class="price">
    <span class="price-amount">$0.40</span><span class="slash"></span><span class="price-unit">ex GST per TRPM</span>
  </div>

  <div class="dims-tab"><span class="tab-label">Dimensions</span><span class="slash"></span></div>
  <div class="dims-box">
    <div class="dims-line"></div>
    <ul class="dims-list">
      <li>100 mm long x 50 mm high x 25 mm wide</li>
      <li>Double sided Class 1A Reflective</li>
      <li>Clear cover for reflective protection</li>
      <li>Available in all white, and red (reflective strip) and white, all yellow and all blue</li>
    </ul>
  </div>

  <div class="range">
    <div class="range-tile"><div class="tile-round" role="img" aria-label="Red, blue and yellow raised pavement markers"></div></div>
    <div class="range-tile"><div class="tile-flat" role="img" aria-label="Silver, gold and white temporary markers"></div></div>
    <div class="range-tile"><div class="tile-adhesive" role="img" aria-label="Bitumen adhesive pads"></div></div>
    <div class="range-tile"><div class="tile-glow" role="img" aria-label="Yellow and glow-in-the-dark pavement markers"></div></div>
  </div>

  <svg class="footer-call" width="882" height="90" viewBox="0 0 882 90">
    <path d="M0 0 H270 C295 0 310 18 310 42 V90 H0 Z" fill="var(--brand-yellow)"/>
    <path d="M0 0 H258 C283 0 298 18 298 42 V90 H0 Z" fill="var(--brand-blue)"/>
  </svg>
  <div class="call-text">
    <div class="call-label">CALL TODAY</div>
    <div class="call-number">02 8417 2530</div>
  </div>

  <div class="company">Kelvoro Lane Ventures Pty Ltd</div>
  <div class="web-pill">www.klvmtq.com</div>
  <div class="contact-strip">
    <span><svg width="13" height="10" viewBox="0 0 13 10"><rect x="0.5" y="0.5" width="12" height="9" fill="none" stroke="var(--brand-blue)"/><path d="M0.5 0.5 L6.5 5.5 L12.5 0.5 M0.5 9.5 L5 5 M12.5 9.5 L8 5" fill="none" stroke="var(--brand-blue)"/></svg>marcus.t@klvsupplyco.com.au</span>
    <span><svg width="13" height="10" viewBox="0 0 13 10"><rect x="0.5" y="0.5" width="12" height="9" fill="none" stroke="var(--brand-blue)"/><path d="M0.5 0.5 L6.5 5.5 L12.5 0.5 M0.5 9.5 L5 5 M12.5 9.5 L8 5" fill="none" stroke="var(--brand-blue)"/></svg>info@klvsupplyco.com.au</span>
  </div>
</main>
</body>
</html>
```